Modern Retail Coffee Label for established Roastery! 17 years!

We are looking for a Retail Coffee Bag Label... JUST THE LABEL TO GO ON AN EXISTING BAG. Our current label is provided and our Logo.. we have had the same Red Bags FOREVER so we are looking for a label to compliment that tradition and to be placed on the bags we have used for 17 years.

We have a retail line of bags with locally roasted coffee. Our business has been around 17years and is in need of a design upgrade! We have a red coffee bag and are looking for a sleek modern label. I will attach a file of our label right now so you can see what it looks like. We are just looking for a more modern version. a few inclusions:

Locally Roasted
100% Arabica Coffee
Heron Kin's Coffee
heronkincoffee.example
logo

The black label with the red and yellow color label is the old one... the new label should be the White background and black border one...

Target Market(s)

Retail Coffee Consumers

Font styles to use
Other font styles liked:
• use what you think. we are located in SW Wisconsin but ship coffee EVERYWHERE

Colors

Designer to choose only greyscale colors for use in the design.

Requirements
Must have
• Locally Roasted (Platteville,WI)
• 100% Arabica Coffee
• heronkincoffee.example
• logo
Nice to have
• Badgers
• "Since 2003"
Should not have
• Any lunabrew or big brand themes

```html
<!DOCTYPE html>
<html lang="en">
<head>
<meta charset="utf-8">
<title>Heron Kin's Coffee – Retail Bag Label</title>
<link href="https://fonts.googleapis.com/css2?family=Anton&family=Oswald:wght@500;600;700&display=swap" rel="stylesheet">
<style>
  :root {
    --roast-brown: #4a1d19;
    --label-white: #ffffff;
    --paper-grey: #ececec;
    --bean-dark: #3b1f14;
    --bean-mid: #6b3d27;
  }
  * { margin: 0; padding: 0; box-sizing: border-box; }
  html, body {
    width: 1022px; height: 1200px; overflow: hidden;
    background: var(--paper-grey);
  }
  .canvas { position: relative; width: 1022px; height: 1200px; }
  .label {
    position: absolute; left: 21px; top: 46px; width: 980px; height: 1108px;
    background: var(--label-white);
    box-shadow: 0 2px 10px rgba(0,0,0,.12);
  }
  .label-frame {
    position: absolute; left: 34px; top: 21px; width: 903px; height: 1079px;
    background: var(--roast-brown);
  }
  .label-panel {
    position: absolute; left: 84px; top: 63px; width: 819px; height: 989px;
    background: var(--label-white);
  }
  .brand-block {
    position: absolute; left: 236px; top: 135px; width: 518px; height: 254px;
    display: flex; flex-direction: column; align-items: center; justify-content: center;
    gap: 14px;
  }
  .brand-name {
    font-family: "Oswald", sans-serif; font-weight: 600;
    font-size: 66px; line-height: 1; letter-spacing: 2px;
    color: var(--roast-brown); text-transform: uppercase; text-align: center;
  }
  .brand-since {
    font-family: "Oswald", sans-serif; font-weight: 600;
    font-size: 22px; letter-spacing: 3px; color: var(--roast-brown);
    text-transform: uppercase;
  }
  .headline {
    position: absolute; left: 105px; width: 820px; top: 438px;
    text-align: center;
    font-family: "Anton", sans-serif; font-size: 112px; line-height: 1.1;
    color: var(--label-white);
    -webkit-text-stroke: 4px var(--roast-brown);
    paint-order: stroke fill;
    text-shadow: 4px 4px 0 var(--roast-brown);
  }
  .location {
    position: absolute; left: 105px; width: 820px; top: 648px;
    text-align: center;
    font-family: "Oswald", sans-serif; font-weight: 700; font-size: 54px; line-height: 1.2;
    color: var(--roast-brown);
  }
  .bean-cluster {
    position: absolute; left: 161px; top: 702px; width: 377px; height: 329px;
    background: radial-gradient(ellipse at 50% 50%, var(--bean-mid) 0%, var(--bean-dark) 55%, rgba(59,31,20,0) 72%);
  }
  .claim-bands { position: absolute; left: 0; top: 0; width: 980px; height: 1108px; }
  .claim-text {
    font-family: "Oswald", sans-serif; font-weight: 500; font-size: 46px;
    fill: var(--label-white); text-anchor: middle;
  }
  .web-address {
    position: absolute; left: 34px; width: 903px; top: 1058px;
    text-align: center;
    font-family: "Oswald", sans-serif; font-weight: 600; font-size: 24px; letter-spacing: 1.5px;
    color: var(--label-white);
  }
</style>
</head>
<body>
<div class="canvas">
  <div class="label">
    <div class="label-frame"></div>
    <div class="label-panel"></div>

    <div class="brand-block">
      <div class="brand-name">Heron Kin's Coffee</div>
      <div class="brand-since">Since 2003</div>
    </div>

    <div class="headline">Locally Roasted</div>
    <div class="location">(Platteville,WI)</div>

    <div class="bean-cluster" role="img" aria-label="Cluster of roasted coffee beans"></div>

    <svg class="claim-bands" viewBox="0 0 980 1108" aria-hidden="false">
      <polygon points="690,740 903,740 903,826 654,826" fill="var(--roast-brown)"/>
      <polygon points="650,835 903,835 903,921 614,921" fill="var(--roast-brown)"/>
      <polygon points="610,930 903,930 903,1023 572,1023" fill="var(--roast-brown)"/>
      <text class="claim-text" x="784" y="800">100%</text>
      <text class="claim-text" x="764" y="895">ARABICA</text>
      <text class="claim-text" x="744" y="993">COFFEE</text>
    </svg>

    <div class="web-address">www.heronkincoffee.example</div>
  </div>
</div>
</body>
</html>
```